Healthcare marketing Website design

This is for a healthcare marketing agency
All details and brief included in the files

I need the design to be incredible!

5 pages to be designed
Home page
About
Portfolio Page
Services
Start your project page

If you need more stock images - download preview images from kelmora pix so I can purchase at a later date

```html
<!DOCTYPE html>
<html lang="en">
<head>
<meta charset="utf-8">
<title>Crestline Health Marketing – Home</title>
<link href="https://fonts.googleapis.com/css2?family=Quicksand:wght@500;600;700&family=Poppins:wght@400;500;600&display=swap" rel="stylesheet">
<style>
:root{
  --navy:#22263a;
  --navy-2:#2c3047;
  --navy-card:#353a55;
  --blue:#2a62c9;
  --cyan:#19a6e6;
  --ink:#1f2333;
  --muted:#6b6f80;
  --light:#f4f4f7;
  --line:#d9dae2;
  --white:#ffffff;
  --peach:#f3d9cc;
}
*{box-sizing:border-box;margin:0;padding:0}
html,body{width:1200px;height:5240px;overflow:hidden}
body{position:relative;background:var(--light);font-family:"Poppins",sans-serif;color:var(--ink)}
.abs{position:absolute}
h1,h2,h3{font-family:"Quicksand",sans-serif}
.btn{display:inline-block;font-size:14px;font-weight:500;padding:11px 26px;border-radius:4px;text-decoration:none}
.btn-primary{background:var(--blue);color:var(--white)}
.btn-outline{border:1px solid var(--white);color:var(--white)}
.btn-cyan{background:var(--cyan);color:var(--white)}
.btn-outline-cyan{border:1px solid var(--cyan);color:var(--cyan);background:var(--white)}

/* hero */
.hero{left:40px;top:0;width:1120px;height:640px;background:linear-gradient(120deg,#2b3a5c 0%,#4a5f86 40%,#8a8f9e 70%,#c9a77a 100%)}
.hero-shade{left:40px;top:0;width:1120px;height:640px;background:linear-gradient(90deg,rgba(20,25,45,.75),rgba(20,25,45,.2))}
.brand{display:flex;align-items:center;gap:10px;font-family:"Quicksand",sans-serif;font-weight:700;font-size:28px;color:var(--white)}
.brand i{width:18px;height:18px;border-radius:50%;background:var(--cyan)}
.nav{left:460px;top:60px;display:flex;gap:32px;font-size:14px;color:var(--white);align-items:center}
.hero-title{left:300px;top:240px;width:520px;font-size:52px;line-height:60px;font-weight:600;color:var(--white)}
.social{left:130px;top:460px;display:flex;flex-direction:column;gap:12px}
.social span{width:28px;height:28px;border-radius:50%;background:var(--white);display:block}

/* intro */
.intro{left:80px;top:740px;width:680px;font-family:"Quicksand",sans-serif;font-size:32px;line-height:44px;font-weight:600;color:var(--blue)}
.band{left:80px;top:930px;width:1040px;height:230px;background:var(--peach);border-radius:20px;border:2px solid #e6c0ad}
.band-photo{left:80px;top:930px;width:380px;height:230px;border-radius:20px 0 0 20px;background:linear-gradient(135deg,#f7e6dc,#e9cdbd)}
.stat{display:flex;gap:14px;align-items:center;width:260px;font-size:13px;line-height:18px;color:var(--ink)}
.stat b{flex:none;width:46px;height:46px;border-radius:50%;background:var(--cyan);color:var(--white);font-size:13px;display:flex;align-items:center;justify-content:center}

/* dark about */
.dark{left:0;width:1200px;background:var(--navy)}
.about-h{left:130px;top:1330px;width:440px;font-size:26px;line-height:34px;color:var(--white);font-weight:700}
.about-p{left:130px;top:1420px;width:470px;font-size:15px;line-height:26px;color:#c4c7d4}
.svc{left:690px;display:flex;gap:40px;align-items:center}
.svc svg{flex:none}
.svc h3{font-size:17px;color:var(--white)}
.svc p{font-size:12px;line-height:18px;color:#b9bccb;width:260px}

/* helping */
.help-h{left:0;top:2100px;width:1200px;text-align:center;font-size:40px;font-weight:600}
.help-p{left:330px;top:2170px;width:540px;text-align:center;font-size:14px;line-height:22px;color:var(--muted)}
.card{width:165px;height:200px;border-radius:18px;background:var(--navy-card);color:var(--white);text-align:center;box-shadow:0 14px 30px rgba(34,38,58,.25);display:flex;flex-direction:column;justify-content:center;gap:8px;font-size:17px}
.card b{font-size:32px;font-family:"Quicksand",sans-serif}
.help-side{left:730px;top:2350px;width:340px;font-size:14px;line-height:22px;color:var(--muted)}

/* testimonials */
.test-h{left:0;top:2830px;width:1200px;text-align:center;font-size:36px;color:var(--white);font-weight:700}
.quote{left:360px;top:2910px;width:480px;height:220px;background:var(--navy-card);border-radius:6px;padding:34px 40px;text-align:center;font-size:13px;line-height:21px;color:#cfd2de;box-shadow:0 10px 0 -4px #2f3450,0 20px 0 -8px #2a2e48}
.quote strong{display:block;margin-top:20px;font-size:13px;letter-spacing:1px;color:var(--white)}
.avatar{width:60px;height:60px;background:linear-gradient(135deg,#8e8a84,#c8b9a6);border-radius:4px}

/* faq */
.faq-h{left:0;top:3510px;width:1200px;text-align:center;font-size:40px;font-weight:700}
.faq{left:230px;width:740px;border-bottom:1px solid var(--line);font-size:18px;font-weight:500;padding-bottom:24px}
.faq p{font-size:14px;line-height:22px;color:var(--muted);font-weight:400;margin-top:20px;width:700px}
.chev{position:absolute;right:10px;top:4px}

/* blog */
.blog-h{left:0;top:4240px;width:1200px;text-align:center;font-size:40px;font-weight:700}
.post{width:290px}
.post .img{height:290px;border-radius:6px}
.post small{display:block;margin-top:18px;font-size:12px;color:#e38b2c}
.post small span{color:var(--muted)}
.post h3{font-family:"Poppins",sans-serif;font-size:19px;font-weight:500;margin-top:4px}
.post a{display:inline-block;margin-top:22px;font-size:14px;color:var(--ink);text-decoration:none;border-bottom:2px solid var(--ink);padding-bottom:6px}

/* footer */
.foot-col h4{font-size:16px;color:var(--white);font-weight:500;margin-bottom:14px}
.foot-col li{list-style:none;font-size:13px;line-height:24px;color:#b9bccb}
.field{width:250px;height:44px;background:var(--navy-2);border-radius:4px;color:#8d91a5;font-size:13px;padding:13px 14px}
.copy{left:130px;top:5150px;font-size:12px;color:#9ea2b4}
</style>
</head>
<body>

<!-- hero -->
<div class="abs hero" role="img" aria-label="Photo of a health professional reviewing charts on a desk with a laptop"></div>
<div class="abs hero-shade"></div>
<div class="abs brand" style="left:130px;top:48px"><i></i>crestline</div>
<nav class="abs nav">
  <span>About</span><span>Portfolio</span><span>Contact Us</span><span>Our Services</span><span>Blog</span>
  <a class="btn btn-primary" style="margin-left:8px">Start Project</a>
</nav>
<h1 class="abs hero-title">Being online: a large opportunity for your practice</h1>
<a class="abs btn btn-primary" style="left:300px;top:436px">Start Project</a>
<div class="abs social"><span></span><span></span><span></span></div>
<svg class="abs" style="left:1020px;top:510px" width="40" height="60" viewBox="0 0 40 60"><path d="M20 2v52M6 40l14 14 14-14" fill="none" stroke="#fff" stroke-width="3"/></svg>
<svg class="abs" style="left:700px;top:560px" width="500" height="320" viewBox="0 0 500 320"><path d="M0 40C120 120 200 40 300 120S460 260 500 240" fill="none" stroke="#c9a8d8" stroke-width="1.5"/><path d="M0 60C130 140 210 60 310 140S470 280 500 260" fill="none" stroke="#d8c1e3" stroke-width="1"/></svg>

<!-- intro -->
<h2 class="abs intro">Don't miss a new opportunity to grow you practice with your online presence.</h2>
<div class="abs band"></div>
<div class="abs band-photo" role="img" aria-label="Illustration of health care icons: a search magnifier, a stethoscope and a syringe"></div>
<div class="abs stat" style="left:480px;top:960px"><b>80%</b>Of internet users search for health information</div>
<div class="abs stat" style="left:800px;top:960px"><b>56%</b>Would like information about a specific health professional</div>
<div class="abs stat" style="left:480px;top:1060px"><b>40%</b>Of individuals look at health related consumer reviews</div>
<div class="abs stat" style="left:800px;top:1060px"><b>41%</b>Of consumers say online presence may impact their choice of health professional</div>

<!-- about -->
<div class="abs dark" style="top:1288px;height:644px"></div>
<h2 class="abs about-h">Crestline Health Marketing: helping those who help others</h2>
<p class="abs about-p">You became a health professional because you wanted to make a difference and you obviously care about patient outcomes. At first things were great and you had plenty of patients but in the last few years there's more competition offering the same types of services and products that you do.<br>We help you build your online assets through :</p>
<a class="abs btn btn-primary" style="left:130px;top:1750px">Start Project</a>
<a class="abs btn btn-outline" style="left:310px;top:1750px">Learn more</a>
<svg class="abs" style="left:730px;top:1400px" width="10" height="360" viewBox="0 0 10 360"><line x1="5" y1="0" x2="5" y2="360" stroke="#3e8fd6" stroke-width="1"/></svg>
<div class="abs svc" style="top:1430px">
  <svg width="90" height="90" viewBox="0 0 90 90"><rect x="19" y="19" width="52" height="52" transform="rotate(45 45 45)" fill="#1e2a4a" stroke="#3e8fd6"/><circle cx="45" cy="45" r="18" fill="var(--blue)"/><path d="M37 45h16M45 37v16" stroke="#fff" stroke-width="2"/></svg>
  <div><h3>Website development</h3><p>Integrate elements and create a landing page in a matter of minutes</p></div>
</div>
<div class="abs svc" style="top:1560px">
  <svg width="90" height="90" viewBox="0 0 90 90"><rect x="19" y="19" width="52" height="52" transform="rotate(45 45 45)" fill="#1e2a4a" stroke="#3e8fd6"/><circle cx="45" cy="45" r="18" fill="var(--blue)"/><path d="M37 49l6-6 4 4 7-8" stroke="#fff" stroke-width="2" fill="none"/></svg>
  <div><h3>Social media marketing</h3><p>Great features for a customisable theme landing page</p></div>
</div>
<div class="abs svc" style="top:1690px">
  <svg width="90" height="90" viewBox="0 0 90 90"><rect x="19" y="19" width="52" height="52" transform="rotate(45 45 45)" fill="#1e2a4a" stroke="#3e8fd6"/><circle cx="45" cy="45" r="18" fill="var(--blue)"/><circle cx="45" cy="45" r="7" stroke="#fff" stroke-width="2" fill="none"/></svg>
  <div><h3>Online Traffic Strategies</h3><p>We help you customise and build your grand landing page</p></div>
</div>

<!-- helping -->
<h2 class="abs help-h">Helping clients since 2015</h2>
<p class="abs help-p">Crestline Health Marketing specialises in helping health professionals like you, stand out from the busy crowd, find new patient and helps you be seen as the go-to person within your industry. Unlike most health professionals who solely rely on word-of-mouth; we use the latest online marketing techniques to grow you and your practice.</p>
<div class="abs card" style="left:140px;top:2390px"><b>25%</b>Ecommerce<br>projects</div>
<div class="abs card" style="left:315px;top:2320px"><b>63%</b>Healthcare and<br>medical</div>
<div class="abs card" style="left:495px;top:2390px"><b>12%</b>Other<br>services</div>
<p class="abs help-side">While our niche has always been in the healthcare industry, Crestline Marketing also has experience in providing solutions for e-commerce partners as well as other professional industries.</p>
<a class="abs btn btn-cyan" style="left:730px;top:2480px">Start Project</a>
<a class="abs btn btn-outline-cyan" style="left:910px;top:2480px">Contact us</a>

<!-- testimonials -->
<div class="abs dark" style="top:2740px;height:620px"></div>
<h2 class="abs test-h">See what our clients say</h2>
<div class="abs quote">Lorem ipsum dolor sit amet, consectetur adipiscing elit, sed do eiusmod tempor incididunt ut labore et dolore magna aliqua. Ut enim ad minim veniam.<br>Duis aute irure dolor in reprehenderit in voluptate velit esse cillum dolore eu fugiat nulla pariatur.<strong>DANA WHITFIELD</strong></div>
<div class="abs avatar" role="img" aria-label="Client portrait" style="left:180px;top:2870px"></div>
<div class="abs avatar" role="img" aria-label="Client portrait" style="left:140px;top:3020px"></div>
<div class="abs avatar" role="img" aria-label="Client portrait" style="left:190px;top:3170px"></div>
<div class="abs avatar" role="img" aria-label="Client portrait" style="left:950px;top:2880px"></div>
<div class="abs avatar" role="img" aria-label="Client portrait" style="left:990px;top:3030px"></div>
<div class="abs avatar" role="img" aria-label="Client portrait" style="left:930px;top:3170px"></div>
<svg class="abs" style="left:540px;top:3310px" width="120" height="6" viewBox="0 0 120 6"><rect width="30" height="4" fill="#fff"/><rect x="40" width="30" height="4" fill="#5a5f7a"/><rect x="80" width="30" height="4" fill="#5a5f7a"/></svg>

<!-- faq -->
<h2 class="abs faq-h">FAQ</h2>
<div class="abs faq" style="top:3630px">Question 1 ?<svg class="chev" width="16" height="10" viewBox="0 0 16 10"><path d="M1 1l7 7 7-7" fill="none" stroke="#888" stroke-width="1.5"/></svg></div>
<div class="abs faq" style="top:3750px">Question 2 ?<svg class="chev" width="16" height="10" viewBox="0 0 16 10"><path d="M1 1l7 7 7-7" fill="none" stroke="#888" stroke-width="1.5"/></svg></div>
<div class="abs faq" style="top:3890px">Question 3 ?<svg class="chev" width="16" height="10" viewBox="0 0 16 10"><path d="M1 9l7-7 7 7" fill="none" stroke="#888" stroke-width="1.5"/></svg><p>Lorem ipsum dolor sit amet, consectetur adipiscing elit, sed do eiusmod tempor incididunt ut labore et dolore magna aliqua. Ut enim ad minim veniam, quis nostrud exercitation.</p></div>

<!-- blog -->
<h2 class="abs blog-h">Blog</h2>
<article class="abs post" style="left:130px;top:4380px"><div class="img" role="img" aria-label="Photo of a woman smiling in a car" style="background:linear-gradient(135deg,#3a3b40,#a9a7a4)"></div><small>SALES <span>· 5 MIN READ</span></small><h3>How to download UI Kit</h3><a>Read more</a></article>
<article class="abs post" style="left:455px;top:4380px"><div class="img" role="img" aria-label="Photo of a person relaxing on a sofa at home" style="background:linear-gradient(135deg,#c9a886,#ece4da)"></div><small>SALES <span>· 5 MIN READ</span></small><h3>How to download UI Kit</h3><a>Read more</a></article>
<article class="abs post" style="left:775px;top:4380px"><div class="img" role="img" aria-label="Photo of a man in a colourful jacket outdoors" style="background:linear-gradient(135deg,#2d6a3c,#d98a2b)"></div><small>SALES <span>· 5 MIN READ</span></small><h3>How to download UI Kit</h3><a>Read more</a></article>

<!-- footer -->
<div class="abs dark" style="top:4810px;height:430px"></div>
<div class="abs brand" style="left:130px;top:4880px"><i></i>crestline</div>
<div class="abs foot-col" style="left:390px;top:4880px"><h4>Pages</h4><ul><li>About</li><li>Portfolio</li><li>Our Services</li><li>Contact us</li><li>Blog</li></ul></div>
<div class="abs foot-col" style="left:545px;top:4880px"><h4>Other</h4><ul><li>Privacy Policy</li><li>Terms and conditions</li><li>&nbsp;</li><li>Our Email :</li><li style="color:var(--cyan)">hello@crestlinemarketing.com</li></ul></div>
<div class="abs foot-col" style="left:820px;top:4880px"><h4>Sign up to our mailing list</h4></div>
<div class="abs field" style="left:820px;top:4925px">Enter email adress</div>
<a class="abs btn btn-primary" style="left:820px;top:4985px;padding:9px 24px">Send</a>
<p class="abs copy">© 2022 Crestline Health Marketing. All Right reserved</p>
<div class="abs" style="left:1000px;top:5145px;display:flex;gap:14px"><span style="width:22px;height:22px;border-radius:50%;border:1px solid #9ea2b4"></span><span style="width:22px;height:22px;border-radius:50%;border:1px solid #9ea2b4"></span><span style="width:22px;height:22px;border-radius:50%;border:1px solid #9ea2b4"></span></div>

</body>
</html>
```